Business Card Design

We would like a business card that utilizes our current logo and keeps with the same feel - elegant and organic. Our farm isn't about mass production, it's about excellence, education, beautiful events and flowers - people, culture, and community.

Target Market(s)

Patrons to our farm who are interested in weddings, events, or our flowers and vegetables.

Contact Information for Business Card

Name, address, cell email (Danielle Hoskins, 2716 Wrenfield Rd, Millbrook, CO 80711, cell 30.412.6638, email danielle@wrenfieldacres.com)

```html
<!DOCTYPE html>
<html lang="en">
<head>
<meta charset="UTF-8">
<title>Wrenfield Acres – Business Card</title>
<link rel="stylesheet" href="https://fonts.googleapis.com/css2?family=Jost:wght@400;600&display=swap">
<style>
  :root {
    --backdrop: #1d1d1d;
    --card-front: #f3f3f1;
    --card-back: #a07c4f;
    --sage: #5f7e67;
    --sage-faint: #d6ded8;
    --tan-faint: #b4916a;
    --cream: #fbf6ee;
    --rule: #d9c6aa;
  }
  * { margin: 0; padding: 0; box-sizing: border-box; }
  html, body {
    width: 1176px;
    height: 1200px;
    overflow: hidden;
    background: var(--backdrop);
    font-family: "Jost", sans-serif;
  }
  .card {
    position: absolute;
    left: 251px;
    width: 674px;
    height: 389px;
    overflow: hidden;
  }
  .card--front { top: 158px; background: var(--card-front); }
  .card--back  { top: 655px; background: var(--card-back); color: var(--cream); }

  .leaf-spray {
    position: absolute;
    border-radius: 40% 60% 50% 50%;
  }
  .card--front .leaf-spray { background: linear-gradient(90deg, rgba(214,222,216,0.4), var(--sage-faint)); }
  .card--back .leaf-spray  { background: linear-gradient(90deg, rgba(180,145,106,0.3), var(--tan-faint)); opacity: 0.7; }
  .leaf-spray--top-right   { left: 478px; top: 43px;  width: 196px; height: 74px; }
  .leaf-spray--bottom-left { left: 0;     top: 250px; width: 215px; height: 95px; }
  .leaf-spray--back-top    { left: 0;     top: 25px;  width: 132px; height: 52px; }
  .leaf-spray--back-bottom { left: 0;     top: 322px; width: 122px; height: 49px; }

  .brand-name {
    position: absolute;
    left: 0;
    width: 100%;
    top: 168px;
    text-align: center;
    font-weight: 400;
    font-size: 42px;
    letter-spacing: 3px;
    color: var(--sage);
  }

  .brand-watermark {
    position: absolute;
    left: 382px;
    top: 160px;
    font-weight: 400;
    font-size: 62px;
    white-space: nowrap;
    color: var(--tan-faint);
  }

  .holder-name {
    position: absolute;
    left: 77px;
    top: 84px;
    font-weight: 600;
    font-size: 26px;
    letter-spacing: 0.3px;
  }
  .holder-rule {
    position: absolute;
    left: 81px;
    top: 135px;
    width: 194px;
    height: 1.5px;
    background: var(--rule);
  }
  .contact-list {
    position: absolute;
    left: 76px;
    top: 168px;
    list-style: none;
    font-size: 17px;
    line-height: 23px;
    letter-spacing: 0.4px;
  }
  .contact-item {
    display: flex;
    align-items: flex-start;
    margin-bottom: 22px;
  }
  .contact-item:nth-child(2) { margin-bottom: 25px; }
  .contact-icon {
    width: 21px;
    height: 21px;
    margin-right: 16px;
    flex: none;
    fill: none;
    stroke: var(--cream);
    stroke-width: 1.4;
    stroke-linecap: round;
    stroke-linejoin: round;
  }
</style>
</head>
<body>

<section class="card card--front" aria-label="Card front">
  <div class="leaf-spray leaf-spray--top-right" role="img" aria-label="Faint leafy branch sprig"></div>
  <div class="leaf-spray leaf-spray--bottom-left" role="img" aria-label="Faint leafy branch sprig"></div>
  <h1 class="brand-name">Wrenfield Acres</h1>
</section>

<section class="card card--back" aria-label="Card back">
  <div class="leaf-spray leaf-spray--back-top" role="img" aria-label="Faint leafy branch sprig"></div>
  <div class="leaf-spray leaf-spray--back-bottom" role="img" aria-label="Faint leafy branch sprig"></div>
  <div class="brand-watermark" aria-hidden="true">Wrenfield</div>

  <h2 class="holder-name">Danielle Hoskins</h2>
  <div class="holder-rule"></div>

  <ul class="contact-list">
    <li class="contact-item">
      <svg class="contact-icon" viewBox="0 0 24 24" aria-hidden="true">
        <path d="M12 22s-7-7.2-7-12.3A7 7 0 0 1 19 9.7C19 14.8 12 22 12 22z"/>
        <circle cx="12" cy="9.7" r="2.6"/>
      </svg>
      <span>2716 Wrenfield Rd,<br>Millbrook, CO 80711.</span>
    </li>
    <li class="contact-item">
      <svg class="contact-icon" viewBox="0 0 24 24" aria-hidden="true">
        <path d="M5 3h3.5l1.8 4.5-2.3 1.5a11 11 0 0 0 7 7l1.5-2.3 4.5 1.8V19a2 2 0 0 1-2 2A17 17 0 0 1 3 5a2 2 0 0 1 2-2z"/>
        <path d="M14.5 3.5a6 6 0 0 1 6 6M14.5 7a2.5 2.5 0 0 1 2.5 2.5"/>
      </svg>
      <span>30.412.6638</span>
    </li>
    <li class="contact-item">
      <svg class="contact-icon" viewBox="0 0 24 24" aria-hidden="true">
        <rect x="2.5" y="5" width="19" height="14" rx="1"/>
        <path d="M2.5 5.5l9.5 7.5 9.5-7.5M2.5 18.5l7-6M21.5 18.5l-7-6"/>
      </svg>
      <span>danielle@wrenfieldacres.com</span>
    </li>
  </ul>
</section>

</body>
</html>
```